Web design for new streaming audio service

We need a homepage design for a new streaming audio service. Our company is called Olvantra, and we’re basically Vidorama for Audiobooks, Stand-Up Comedy, Lectures, Language Learning, etc. Essentially like Tunelark for everything audio EXCEPT music.
You don’t have to code the homepage (Design Only), but it should include 3 different designs to work with 1) Web; 2) Phones; 3) Tablets.
Below is a link to a mockup of the web version which gives a good idea of what elements we want. This is just a mockup and we want you to improve it.
Once you download the mockup, please refer to the more detailed instructions below:
The following outlines the design project for the Olvantra homepage. We have provided a rough mockup of the homepage layout that gives you a general idea of what we’re going for. There are a few elements that we are attached to, and many others where you have complete creative freedom to do whatever you think looks good.
The ZIP file includes the following:
* Mockup to see what we have in mind (olvantra-homepage-mockup.jpg)
* Text used (olvantra-homepage-text.txt)
* Raw image of actor (olvantra-actor1.jpg)
* Raw images for samples (olvantra-sample-[name].jpg)
Although we have only provided a mockup layout for the web version, we also need you to provide a mobile phone and a tablet version of the design also. It’s very possible the tablet version may be substantially similar to the web version, but the mobile phone version will likely be much different.
All of the raw files are included in the attached ZIP file. Please use our photographs and text as provided although cropping, sizing, etc. is flexible per the instructions below.
Display Requirements:
* Web Version - Minimum resolution 1024x768 (72 dpi) but should look good on 1920x1080 (72 dpi) - Page should be designed to scale to look acceptable in all resolutions in between.
* Phone Version - Minimum Zentro 4 - 640x960 (326 dpi) but should look good on Korvel Nimbus Q5 - 1920x1080 (441 dpi) - Page should be designed to scale to look acceptable in all resolutions and devices in between.
* Tablet Version - Minimum Pagewick Ember LX 7” - 1280x800 (216 dpi) but should also look good on a Slato Breeze - 2048x1536 (264 dpi) - Page should be designed to scale to look acceptable in all resolutions and devices in between.
Above the Fold - We want to make sure the Olvantra logo, Member Login Link, Large Photo, Headline, Price, Button, and the first row of sample images are all “Above the fold”. As a general guideline, this means 600 pixels high on a 1024x768 72 dpi web screen. This requirement is less important on Phone versions.
Top Logo Bar - We want to retain the blue bar with the Olvantra logo on the page, although we are open to a different size, shape and positioning if it greatly enhances the design. Please use the standard logo color, although you are welcome to use either the horizontal or vertical orientation of the logo based on your design.
Text color, font and size - Feel free to design the text in anyway you choose as long as the text is readable on the target platforms.
Buttons - Feel free to use any size, shape and colors for the buttons as long as they are obvious and clickable relative to the page. The only exception is the Chatterly button should follow the Chatterly color scheme and logo treatment (the mockup doesn’t seem 100% correct.)
Top Photograph - We want to retain the large photograph across the top of the screen although final shape and dimensions are flexible.
Size and shape of content samples (i.e. Audiobooks, Stand-Up Comedy, etc.) - Feel free to design the content samples in anyway you choose.
Three Sales Points (i.e. Listen on your Zentro…, All you can enjoy…, etc.) - The Three Sales Points are envisioned to each have a corresponding illustration which you should provide and have rights for. The placeholder is represented by a square next to the text. The color size and shape of these elements are flexible and can be designed in any way you choose.
Opt-in form - Feel free to design the opt-in form in anyway you choose as long as the text is readable and the interactivity is obvious on the target platforms.
Text links and copyright notice - Feel free to design the bottom of the page text links and copyright notice in anyway you choose.
Additional colors, graphic design elements, etc. - Feel free to use any additional colors, graphic design elements, etc. to support your design.

```html
<!DOCTYPE html>
<html lang="en">
<head>
<meta charset="utf-8">
<title>Olvantra — Web, Tablet and Phone Homepage</title>
<link rel="stylesheet" href="https://fonts.googleapis.com/css2?family=Lato:wght@300;400;700&display=swap">
<style>
  :root {
    --stage-bg: #eeeff0;
    --brand-blue: #5aa8d3;
    --headline-blue: #4a9fd1;
    --button-blue: #4e9fcf;
    --nav-underline: #1f4e68;
    --white: #ffffff;
    --ink: #2b2b2b;
    --muted: #8a8f94;
    --note-blue: #6aaed6;
    --field-line: #c9d3da;
  }
  * { box-sizing: border-box; margin: 0; padding: 0; }
  html, body {
    width: 1200px;
    height: 480px;
    overflow: hidden;
    background: var(--stage-bg);
    font-family: "Lato", Arial, sans-serif;
  }
  .stage { position: relative; width: 1200px; height: 480px; }

  .screen {
    position: absolute;
    background: var(--white);
    overflow: hidden;
  }
  .screen > * { position: absolute; }

  .top-bar { left: 0; top: 0; width: 100%; background: var(--brand-blue); }
  .top-bar > * { position: absolute; color: var(--white); white-space: nowrap; }
  .brand { display: flex; align-items: center; font-weight: 700; }
  .brand-dot { border-radius: 50%; background: var(--white); flex: none; }
  .main-nav { display: flex; list-style: none; }
  .main-nav li { position: relative; }
  .main-nav li.is-active::after {
    content: ""; position: absolute; left: -3px; right: -3px;
    background: var(--nav-underline);
  }

  .hero { left: 0; width: 100%; overflow: hidden; }
  .hero-photo {
    position: absolute; inset: 0;
    background:
      radial-gradient(ellipse 22% 38% at 63% 42%, #d7a583 0%, rgba(215,165,131,0) 100%),
      radial-gradient(ellipse 45% 26% at 60% 100%, #3d5570 0%, rgba(61,85,112,0) 100%),
      linear-gradient(90deg, #f4f5f6 0%, #eceeef 40%, #d9d2cb 62%, #cdc1b7 80%, #e2e4e6 100%);
  }
  .hero-copy { position: absolute; white-space: nowrap; }
  .hero-headline { color: var(--headline-blue); font-weight: 400; }
  .hero-price { color: var(--headline-blue); font-weight: 300; }
  .trial-button {
    display: inline-block; background: var(--button-blue); color: var(--white);
    text-align: center; border-radius: 1px;
  }
  .trial-note { color: var(--note-blue); letter-spacing: 0.3px; }
  .slider-arrow { position: absolute; }
  .slider-dots { position: absolute; display: flex; align-items: center; transform: translateX(-50%); }
  .slider-dots span { border-radius: 50%; background: var(--white); }
  .slider-dots span.is-current { background: transparent; border: 1px solid var(--white); }

  .samples-heading {
    left: 0; width: 100%; text-align: center; color: var(--ink);
    font-weight: 300; white-space: nowrap;
  }
  .sample-row { display: flex; }
  .sample-cover { flex: none; }
  .cover-noir { background: linear-gradient(180deg, #2e3338, #4b5358); }
  .cover-comedy { background: linear-gradient(160deg, #b5532f, #7c8a5a); }
  .cover-language { background: linear-gradient(180deg, #1d6fb0, #0f2e52); }
  .cover-talk { background: linear-gradient(180deg, #d9c9a8, #8fb26a); }
  .cover-sunset { background: linear-gradient(180deg, #e58a3a, #7b3b6e); }
  .cover-ocean { background: linear-gradient(180deg, #2aa0c8, #1b4f8a); }
  .cover-stage { background: linear-gradient(180deg, #a03a4f, #3b1f3c); }
  .cover-city { background: linear-gradient(180deg, #d05a2a, #f0b24a); }

  /* ---------- Desktop ---------- */
  .screen-web { left: 379px; top: 50px; width: 640px; height: 360px; z-index: 2; }
  .screen-web .top-bar { height: 63px; }
  .screen-web .brand { left: 96px; top: 14px; font-size: 26px; gap: 8px; }
  .screen-web .brand-dot { width: 26px; height: 26px; }
  .screen-web .members-login { right: 87px; top: 21px; font-size: 10.5px; }
  .screen-web .main-nav { right: 86px; top: 42px; gap: 11px; font-size: 8.6px; }
  .screen-web .main-nav li.is-active::after { bottom: -9px; height: 4px; }
  .screen-web .hero { top: 63px; height: 249px; }
  .screen-web .hero-copy { left: 96px; top: 33px; }
  .screen-web .hero-headline { font-size: 24px; line-height: 38px; }
  .screen-web .hero-price { font-size: 15px; line-height: 18px; }
  .screen-web .trial-button { margin-top: 13px; width: 96px; padding: 8px 0; font-size: 8px; }
  .screen-web .trial-note { margin-top: 8px; font-size: 5.5px; }
  .screen-web .slider-arrow { top: 90px; width: 19px; height: 19px; }
  .screen-web .slider-arrow.prev { left: 58px; }
  .screen-web .slider-arrow.next { right: 58px; }
  .screen-web .slider-dots { left: 318px; bottom: 18px; gap: 4px; }
  .screen-web .slider-dots span { width: 5px; height: 5px; }
  .screen-web .slider-dots span.is-current { width: 8px; height: 8px; }
  .screen-web .samples-heading { top: 325px; font-size: 19px; }

  /* ---------- Tablet ---------- */
  .screen-tablet { left: 80px; top: 143px; width: 300px; height: 222px; z-index: 1; }
  .screen-tablet .top-bar { height: 27px; }
  .screen-tablet .brand { left: 45px; top: 6px; font-size: 12px; gap: 4px; }
  .screen-tablet .brand-dot { width: 12px; height: 12px; }
  .screen-tablet .members-login { right: 30px; top: 7px; font-size: 4.6px; }
  .screen-tablet .main-nav { right: 30px; top: 17px; gap: 5px; font-size: 3.9px; }
  .screen-tablet .main-nav li.is-active::after { bottom: -5px; height: 2px; }
  .screen-tablet .hero { top: 27px; height: 115px; }
  .screen-tablet .hero-copy { left: 45px; top: 14px; }
  .screen-tablet .hero-headline { font-size: 11px; line-height: 18px; }
  .screen-tablet .hero-price { font-size: 6.5px; line-height: 8px; }
  .screen-tablet .trial-button { margin-top: 6px; width: 45px; padding: 4px 0; font-size: 3.6px; }
  .screen-tablet .slider-arrow { top: 38px; width: 9px; height: 9px; left: 27px; }
  .screen-tablet .slider-dots { left: 149px; bottom: 10px; gap: 2px; }
  .screen-tablet .slider-dots span { width: 3px; height: 3px; }
  .screen-tablet .slider-dots span.is-current { width: 4px; height: 4px; }
  .screen-tablet .samples-heading { top: 148px; font-size: 9px; }
  .screen-tablet .sample-row { left: 40px; top: 168px; gap: 4px; }
  .screen-tablet .sample-cover { width: 52px; height: 51px; }

  /* ---------- Phone ---------- */
  .screen-phone { left: 1025px; top: 183px; width: 111px; height: 210px; }
  .screen-phone .top-bar { height: 12px; }
  .screen-phone .brand { left: 12px; top: 3px; font-size: 5px; gap: 2px; }
  .screen-phone .brand-dot { width: 5px; height: 5px; }
  .screen-phone .hero { top: 12px; height: 43px; }
  .screen-phone .hero-copy { left: 6px; top: 7px; }
  .screen-phone .hero-headline { font-size: 4.6px; line-height: 7px; }
  .screen-phone .samples-heading { top: 58px; font-size: 3.4px; }
  .screen-phone .sample-grid { left: 14px; top: 66px; display: grid; grid-template-columns: repeat(4, 19px); gap: 3px; }
  .screen-phone .sample-cover { width: 19px; height: 19px; }
  .screen-phone .sales-points { left: 8px; top: 116px; width: 95px; display: flex; justify-content: space-between; }
  .screen-phone .sales-point { width: 28px; text-align: center; font-size: 2.8px; line-height: 3.6px; color: var(--muted); }
  .screen-phone .sales-icon { width: 11px; height: 8px; margin: 0 auto 2px; background: var(--brand-blue); }
  .screen-phone .opt-in { left: 8px; top: 140px; width: 95px; display: flex; justify-content: space-between; }
  .screen-phone .opt-in-title { font-size: 3.6px; color: var(--ink); line-height: 5px; }
  .screen-phone .opt-in-fields { width: 42px; }
  .screen-phone .opt-in-field { height: 5px; border: 0.5px solid var(--field-line); margin-bottom: 2px; font-size: 2.4px; color: var(--muted); padding-left: 1px; line-height: 4px; }
  .screen-phone .opt-in-button { height: 6px; background: var(--button-blue); }
</style>
</head>
<body>
<div class="stage">

  <!-- Tablet view -->
  <div class="screen screen-tablet">
    <header class="top-bar">
      <div class="brand"><span class="brand-dot"></span>Olvantra</div>
      <div class="members-login">Members Login</div>
      <ul class="main-nav">
        <li class="is-active">Home</li><li>Sections</li><li>Privacy Policy</li>
        <li>Terms of Services</li><li>Contact Us</li><li>Help</li>
      </ul>
    </header>
    <section class="hero">
      <div class="hero-photo" role="img" aria-label="Photo of a smiling young man wearing headphones, looking at his phone"></div>
      <div class="hero-copy">
        <h1 class="hero-headline">Unlimited Listening!<br>Wherever You Are!</h1>
        <p class="hero-price">Only $9.99 per month</p>
        <span class="trial-button">START YOUR FREE TRIAL</span>
      </div>
      <svg class="slider-arrow prev" viewBox="0 0 34 34" aria-hidden="true">
        <circle cx="17" cy="17" r="15" fill="none" stroke="#4a9fd1" stroke-width="2.5"/>
        <polyline points="20,10 13,17 20,24" fill="none" stroke="#4a9fd1" stroke-width="2.5"/>
      </svg>
      <div class="slider-dots"><span class="is-current"></span><span></span><span></span><span></span></div>
    </section>
    <h2 class="samples-heading">A sample of what you can listen to on Olvantra</h2>
    <div class="sample-row">
      <div class="sample-cover cover-noir" role="img" aria-label="Audiobook cover artwork"></div>
      <div class="sample-cover cover-comedy" role="img" aria-label="Stand-up comedy cover artwork"></div>
      <div class="sample-cover cover-language" role="img" aria-label="Language course cover artwork"></div>
      <div class="sample-cover cover-talk" role="img" aria-label="Lecture cover artwork"></div>
    </div>
  </div>

  <!-- Web view -->
  <div class="screen screen-web">
    <header class="top-bar">
      <div class="brand"><span class="brand-dot"></span>Olvantra</div>
      <div class="members-login">Members Login</div>
      <ul class="main-nav">
        <li class="is-active">Home</li><li>Sections</li><li>Privacy Policy</li>
        <li>Terms of Services</li><li>Contact Us</li><li>Help</li>
      </ul>
    </header>
    <section class="hero">
      <div class="hero-photo" role="img" aria-label="Photo of a smiling young man wearing headphones, looking at his phone"></div>
      <div class="hero-copy">
        <h1 class="hero-headline">Unlimited Listening!<br>Wherever You Are!</h1>
        <p class="hero-price">Only $9.99 per month</p>
        <span class="trial-button">START YOUR FREE TRIAL</span>
        <p class="trial-note">* CREDIT CARD NOT REQUIRED</p>
      </div>
      <svg class="slider-arrow prev" viewBox="0 0 34 34" aria-hidden="true">
        <circle cx="17" cy="17" r="15" fill="none" stroke="#4a9fd1" stroke-width="2"/>
        <polyline points="20,10 13,17 20,24" fill="none" stroke="#4a9fd1" stroke-width="2"/>
      </svg>
      <svg class="slider-arrow next" viewBox="0 0 34 34" aria-hidden="true">
        <circle cx="17" cy="17" r="15" fill="none" stroke="#4a9fd1" stroke-width="2"/>
        <polyline points="14,10 21,17 14,24" fill="none" stroke="#4a9fd1" stroke-width="2"/>
      </svg>
      <div class="slider-dots"><span class="is-current"></span><span></span><span></span><span></span></div>
    </section>
    <h2 class="samples-heading">A sample of what you can listen to on Olvantra</h2>
  </div>

  <!-- Phone view -->
  <div class="screen screen-phone">
    <header class="top-bar">
      <div class="brand"><span class="brand-dot"></span>Olvantra</div>
    </header>
    <section class="hero">
      <div class="hero-photo" role="img" aria-label="Photo of a smiling young man wearing headphones, looking at his phone"></div>
      <div class="hero-copy">
        <h1 class="hero-headline">Unlimited Listening!<br>Wherever You Are!</h1>
      </div>
    </section>
    <h2 class="samples-heading">A sample of what you can listen to on Olvantra</h2>
    <div class="sample-grid">
      <div class="sample-cover cover-noir" role="img" aria-label="Audiobook cover artwork"></div>
      <div class="sample-cover cover-comedy" role="img" aria-label="Stand-up comedy cover artwork"></div>
      <div class="sample-cover cover-language" role="img" aria-label="Language course cover artwork"></div>
      <div class="sample-cover cover-talk" role="img" aria-label="Lecture cover artwork"></div>
      <div class="sample-cover cover-sunset" role="img" aria-label="Audiobook cover artwork"></div>
      <div class="sample-cover cover-ocean" role="img" aria-label="Podcast cover artwork"></div>
      <div class="sample-cover cover-stage" role="img" aria-label="Comedy special cover artwork"></div>
      <div class="sample-cover cover-city" role="img" aria-label="Travel guide cover artwork"></div>
    </div>
    <div class="sales-points">
      <div class="sales-point"><div class="sales-icon"></div>Listen on your Zentro</div>
      <div class="sales-point"><div class="sales-icon"></div>All you can enjoy</div>
      <div class="sales-point"><div class="sales-icon"></div>No contracts ever</div>
    </div>
    <div class="opt-in">
      <p class="opt-in-title">Start Your Free Trial</p>
      <div class="opt-in-fields">
        <div class="opt-in-field">Your name</div>
        <div class="opt-in-field">Email address</div>
        <div class="opt-in-button"></div>
      </div>
    </div>
  </div>

</div>
</body>
</html>
```